Motor Vault Website - Part of the Brantley Group

A complimentary website is required for the launch of a 'Motor Vault' - a new service launched by industry renowned BRANTLEY. Motor Vault is an industry-first brand that designs and builds unique subterranean car parks for private residential homes in London and the influential counties within the UK. Please see here the direction of a new BRANTLEY Website - we would like Motor Vault to be complimentary and sit alongside BRANTLEY harmoniously - https://www.brantleyhq.example/brantley-nu-staging Brantley have some images, but whilst more professional images are in production - we have also attached pixmoor photos- named clearly as pixmoor. **Attached files include JPEG, .eps of logo and Brantley library images and Pixmoor Library Images - two versions of logo dependent on background colour. - Website needs to be sleek, chic and masculine.- Colour Palette - Grey/ Black/ White - Same visiual journey as Brantley website- Required areas within the sit include - About Us / Our Work / Contact Page

Target Market(s)

Luxury
Men

Number of Pages Required

2 page

Font styles to use
Sans Serif

Colors
e8e8e8
757575
1b1b1b
000000
9d9d9d
cbcbcb
f5f5f5

Requirements
Must have
• Complimentary of this site - https://www.brantleyhq.example/brantley-nu-staging
Should not have
• Colour

```html
<!DOCTYPE html>
<html lang="en">
<head>
<meta charset="utf-8">
<title>Motor Vault — Part of the Brantley Group</title>
<link href="https://fonts.googleapis.com/css2?family=Josefin+Sans:wght@300;400;600&family=Cormorant+Garamond:wght@600&display=swap" rel="stylesheet">
<style>
  :root {
    --black: #000000;
    --ink: #1b1b1b;
    --footer: #222222;
    --mid: #757575;
    --soft: #9d9d9d;
    --pale: #cbcbcb;
    --light: #e8e8e8;
    --white: #ffffff;
    --sans: 'Josefin Sans', sans-serif;
    --serif: 'Cormorant Garamond', serif;
  }
  * { margin: 0; padding: 0; box-sizing: border-box; }
  html, body { width: 738px; height: 1200px; overflow: hidden; background: var(--white); }
  .page { position: relative; width: 738px; height: 1200px; font-family: var(--sans); color: var(--ink); }

  .brand { position: absolute; display: flex; flex-direction: column; align-items: flex-end; }
  .brand-row { display: flex; align-items: center; gap: 7px; }
  .brand-mark { width: 0.7em; height: 0.7em; background: currentColor; }
  .brand-name { font-family: var(--sans); font-weight: 600; letter-spacing: 0.02em; line-height: 1; white-space: nowrap; }
  .brand-tag { font-family: var(--sans); font-weight: 300; text-transform: uppercase; white-space: nowrap; }

  .hero { position: absolute; left: 0; top: 0; width: 738px; height: 414px;
    background: radial-gradient(ellipse at 50% 55%, #4a4a4a 0%, #262626 45%, #0b0b0b 100%); }
  .hero .brand { left: 198px; top: 182px; color: var(--light); font-size: 38px; }
  .hero .brand-tag { font-size: 7px; color: var(--soft); margin-top: 4px; letter-spacing: 0.02em; }

  .nav { position: absolute; left: 0; top: 414px; width: 738px; height: 76px; background: var(--white);
    box-shadow: 0 4px 10px rgba(0,0,0,0.08); z-index: 2; }
  .nav .brand { left: 38px; top: 22px; color: var(--ink); font-size: 25px; }
  .nav .brand-tag { font-size: 5.5px; color: var(--mid); margin-top: 3px; }
  .nav-links { position: absolute; top: 37px; left: 362px; list-style: none; font-size: 11.5px; letter-spacing: 0.03em; }
  .nav-links li { position: absolute; top: 0; white-space: nowrap; }
  .nav-links .current { text-decoration: underline; text-underline-offset: 4px; }

  .intro { position: absolute; left: 0; top: 490px; width: 738px; height: 190px; text-align: center; }
  .intro h1 { margin-top: 52px; font-family: var(--serif); font-weight: 600; font-size: 23px; line-height: 27px;
    letter-spacing: 0.12em; color: var(--ink); }

  .slider { position: absolute; left: 0; top: 680px; width: 738px; height: 318px; color: var(--white); text-align: center;
    background: radial-gradient(ellipse at 55% 40%, #4c4c4c 0%, #2a2a2a 50%, #111 100%); }
  .slider h2 { position: absolute; top: 104px; width: 100%; font-family: var(--serif); font-weight: 600; font-size: 24px; letter-spacing: 0.17em; white-space: nowrap; }
  .slider p { position: absolute; top: 152px; left: 0; width: 100%; font-size: 12px; line-height: 19px; font-weight: 300; white-space: nowrap; }
  .slider-arrow { position: absolute; top: 148px; width: 18px; height: 22px; }
  .dot { position: absolute; top: 290px; width: 9px; height: 9px; border-radius: 50%; background: var(--white); }
  .dot.active { background: transparent; border: 1px solid var(--white); }

  .footer { position: absolute; left: 0; top: 998px; width: 738px; height: 202px; background: var(--footer); text-align: center; }
  .footer .brand { left: 260px; top: 26px; color: var(--light); font-size: 25px; }
  .footer .brand-tag { font-size: 5.5px; color: var(--soft); margin-top: 3px; }
  .social { position: absolute; top: 80px; left: 0; width: 100%; height: 24px; }
  .social span { position: absolute; width: 20px; height: 20px; background: #333; transform: rotate(45deg); }
  .footer-line { position: absolute; width: 100%; font-size: 8px; letter-spacing: 0.18em; color: var(--mid); text-transform: uppercase; }
</style>
</head>
<body>
<div class="page">

  <header class="hero" role="img" aria-label="Empty concrete underground garage lit from above">
    <div class="brand">
      <div class="brand-row"><span class="brand-mark"></span><span class="brand-name">MOTOR VAULT</span></div>
      <span class="brand-tag">Part of the Brantley Group</span>
    </div>
  </header>

  <nav class="nav">
    <div class="brand">
      <div class="brand-row"><span class="brand-mark"></span><span class="brand-name">MOTOR VAULT</span></div>
      <span class="brand-tag">Part of the Brantley Group</span>
    </div>
    <ul class="nav-links">
      <li class="current" style="left:0">HOME</li>
      <li style="left:66px">ABOUT</li>
      <li style="left:134px">PROJECTS</li>
      <li style="left:220px">NEWS</li>
      <li style="left:281px">CONTACT</li>
    </ul>
  </nav>

  <section class="intro">
    <h1>INDUSTRY-FIRST BRAND THAT DESIGNS<br>AND BUILDS UNIQUE SUBTERRANEAN<br>CAR PARKS</h1>
  </section>

  <section class="slider" role="img" aria-label="Overhead view of a worker welding inside a timber-shored excavation">
    <h2>DELIVERIG TURKNEY SOLUTIONS</h2>
    <p>Lorem ipsum dolor sit amet, consectetur adipiscing elit, sed do eiusmod tempor<br>incididunt ut labore et dolore magna aliqua. Quis ipsum suspendisse ultrices<br>gravida. Risus commodo viverra maecenas accumsan lacus vel facilisis.</p>
    <svg class="slider-arrow" style="left:22px" viewBox="0 0 18 22"><polyline points="14,2 5,11 14,20" fill="none" stroke="#fff" stroke-width="3.5"/></svg>
    <svg class="slider-arrow" style="left:698px" viewBox="0 0 18 22"><polyline points="4,2 13,11 4,20" fill="none" stroke="#fff" stroke-width="3.5"/></svg>
    <span class="dot active" style="left:341px"></span>
    <span class="dot" style="left:356px"></span>
    <span class="dot" style="left:371px"></span>
    <span class="dot" style="left:386px"></span>
  </section>

  <footer class="footer">
    <div class="brand">
      <div class="brand-row"><span class="brand-mark"></span><span class="brand-name">MOTOR VAULT</span></div>
      <span class="brand-tag">Part of the Brantley Group</span>
    </div>
    <div class="social" aria-label="Social links">
      <span style="left:294px"></span>
      <span style="left:337px"></span>
      <span style="left:380px"></span>
      <span style="left:423px"></span>
    </div>
    <p class="footer-line" style="top:137px">48 Harcourt Yard, London, W9 1QT | Tel: 0207 555 0142</p>
    <p class="footer-line" style="top:160px">Copyright © Brantley 2018. Terms and Conditions | Privacy Policy</p>
  </footer>

</div>
</body>
</html>
```